Kolibri-Stube
Ich bin sehr zufrieden mit dem Flyer, Plakat und Logo, welches ich für einen zahlbaren Preis bekommen habe. quorvix hat die Korrekturvorschläge sehr gut und immer zügig umgesetzt und ein wirklich gelungenes Resultat produzier.
Zielgruppe
Logo/Sloagan: Kolibri-Stube
Branchen: Kunst/Kultur und Bildung
Ich biete eine Kolibri-Stube an, in der bis 12 Personen quartalsweise über ein Jahr hinweg an einer Erzählung ode einem Roman arbeiten. Das Genre kann frei gewählt werden. Ob Kriminal-, Fantasy oder Liebesroman, Autobiografie oder Dokufiktion, die Grundlagen eines spannenden Textes sind die selben.
Zielgruppe sind Jugendliche bis Senioren, die gerne eine lägere Erzählung oder einen Roman schreiben möchten.
Aufgabenstellung
Siehe Design-Briefing (PDF) mit Inhalt für Flyertext
Wichtig ist mir der Flyer A4 gefaltet (zu A5 oder 2x gefaltet) oder A5, alle beidseits bedruckt und je nachdem, wie sie den Inhalt verteilen möchten.
Ich bin offen für Design- und Formatvorschläge.
- Ein Plakat A4/A3, welches mit der Vorderseite des Flyers grösstenteils übereinstimmt. Wenn ich ein InDesign oder Photoshop mit Layern kriege, kann ich den Text des Plakats selber ergänzen/bearbeiten.
Ich habe neben dem Briefing und einem Foto von mir noch ein paar Bilder hochgeladen, deren Stil mir gefällt. Habe aber NICHT deren Rechte. Bilder müssten also durch Sie gefunden werden, ich kann diese aber extra bezahlen, bitte Preis dafür deklarieren.
Logo brauche ich noch keines.
Besten Dank für Ihre Bemühungen

```html
<!DOCTYPE html>
<html lang="de">
<head>
<meta charset="utf-8">
<title>Kolibri-Stube – Plakat</title>
<link href="https://fonts.googleapis.com/css2?family=Yanone+Kaffeesatz:wght@200;300;400;500;600;700&display=swap" rel="stylesheet">
<style>
  :root {
    --wine: #4a0000;
    --gold: #f0c400;
    --paper: #ffffff;
    --ink: #000000;
  }
  * { box-sizing: border-box; margin: 0; padding: 0; }
  html, body { width: 849px; height: 1200px; overflow: hidden; }
  body { font-family: "Yanone Kaffeesatz", sans-serif; background: var(--paper); }
  .poster {
    position: relative;
    width: 849px; height: 1200px;
    background: linear-gradient(to bottom, var(--paper) 0 400px, var(--wine) 400px 100%);
    overflow: hidden;
  }
  .rule { position: absolute; background: var(--gold); }
  .rule--top { left: 171px; top: 59px; width: 560px; height: 2px; }
  .rule--right { left: 787px; top: 120px; width: 2px; height: 480px; }
  .rule--left { left: 59px; top: 204px; width: 2px; height: 876px; }
  .rule--bottom { left: 120px; top: 1138px; width: 366px; height: 2px; }

  .title-card {
    position: absolute;
    left: 78px; top: 109px; width: 408px; height: 623px;
    background: var(--paper);
    border: 1.5px solid var(--ink);
    box-shadow: 4px 4px 8px rgba(0,0,0,.3);
  }
  .title-card__name {
    position: absolute;
    left: 40px; top: 40px; width: 350px;
    font-weight: 600;
    font-size: 118px;
    line-height: 118px;
    color: var(--ink);
    letter-spacing: 6px;
  }
  .title-card__line { display: block; white-space: nowrap; }
  .feather {
    position: absolute;
    left: 175px; top: 560px; width: 360px; height: 120px;
    background: var(--gold);
    border-radius: 60% 40% 50% 50% / 70% 60% 40% 30%;
    transform: rotate(-17deg);
  }
  .tagline {
    position: absolute;
    left: 200px; top: 748px; width: 288px;
    color: var(--paper);
    font-weight: 500;
    font-size: 38px;
    line-height: 46px;
  }
  .tagline__line {
    display: block;
    white-space: nowrap;
    text-align: justify;
    text-align-last: justify;
  }
  .web {
    position: absolute;
    left: 96px; top: 1078px;
    color: var(--paper);
    font-weight: 500;
    font-size: 38px;
    line-height: 46px;
  }
  .note {
    position: absolute;
    left: 524px; width: 265px;
    background: var(--paper);
    padding: 10px 14px;
    color: var(--ink);
    font-weight: 300;
    font-size: 21px;
    line-height: 25.3px;
    text-align: justify;
    hyphens: manual;
  }
  .note strong { font-weight: 500; }
  .note--question { top: 631px; height: 300px; }
  .note--offer { top: 948px; height: 165px; line-height: 24px; padding-top: 11px; }
  .note__line { display: block; text-align: left; }
  .note__author { display: block; font-size: 12px; line-height: 18px; margin-top: 4px; text-align: left; }
</style>
</head>
<body>
<main class="poster">
  <div class="rule rule--top"></div>
  <div class="rule rule--right"></div>
  <div class="rule rule--left"></div>
  <div class="rule rule--bottom"></div>

  <section class="title-card">
    <h1 class="title-card__name">
      <span class="title-card__line">Kolibri-</span>
      <span class="title-card__line">Stube</span>
    </h1>
  </section>

  <div class="feather" role="img" aria-label="Goldgelbe Schreibfeder als Illustration"></div>

  <p class="tagline">
    <span class="tagline__line">Mit der Kolibri-Stube</span>
    <span class="tagline__line">zu Ihrem eigenen Roman</span>
  </p>

  <p class="web">www.kolibri-stube-beispiel.ch</p>

  <aside class="note note--question">
    Haben Sie eine erste <strong>Idee</strong> für eine Erzählung oder einen Roman? Eine lebhafte <strong>Fantasie</strong> für das Ausser&shy;ordentliche oder <strong>ungewöhnlich Gewöhnliche?</strong> Oder ein <strong>reiches Leben,</strong> aus dessen Quelle Sie für Ihre Geschichte schöpfen können? Und möchten Sie den zukünftigen Leserinnen und Lesern <strong>Ihren geis&shy;tigen Schatz in Form eines Buches</strong> schenken?
  </aside>

  <aside class="note note--offer">
    <span class="note__line">Ich helfe Ihnen weiter!</span>
    Denn die <strong>Schreibkunst fusst wie alle Künste nicht nur auf Genie, sondern in erster Linie auf Handwerk, dass Ich Ihnen beibringen kann.</strong>
    <span class="note__author">Dr. Lena Varonek</span>
  </aside>
</main>
</body>
</html>
```